New Website for Belcourt Manor at www.belcourt.com.au

A new logo has been designed (through pixel forge) and we now want to align the look and feel of our website at www.belcourt.com.au to the new logo. The content and page names (e.g. Grounds) will remain largely unchanged for the new site, so please submit a new look "Home" page, using our new logo, current text and any photos you choose from the existing gallery at our website. I have also attached the current "Home" page photos.

Industry/Entity Type

Accommodation

Number of Pages Required

1 page

Requirements
Must have
• Logo to be presented on white background.

```html
<!DOCTYPE html>
<html lang="en">
<head>
<meta charset="utf-8">
<title>Belcourt Manor – Home</title>
<link href="https://fonts.googleapis.com/css2?family=Lato:ital,wght@0,300;0,400;1,400&family=Raleway:wght@300&display=swap" rel="stylesheet">
<style>
:root{
  --white:#ffffff;
  --brand-blue:#1a7fc4;
  --link-blue:#0b62b0;
  --text-grey:#6f6f6f;
  --heading-grey:#6a6a6a;
  --nav-band-top:#8aa3bd;
  --nav-band-bottom:#b9c9d9;
  --accent-orange:#ee5a24;
  --accent-gold:#d08a3c;
  --footer-link:#8a8a8a;
}
*{margin:0;padding:0;box-sizing:border-box}
html,body{width:1200px;height:1079px;overflow:hidden;background:var(--white)}
body{font-family:'Lato',sans-serif;color:var(--text-grey);position:relative}
.container{position:absolute;left:128px;width:942px}

.site-header{position:absolute;top:0;left:0;width:1200px;height:77px;background:var(--white)}
.brand{position:absolute;left:128px;top:20px;display:flex;align-items:center;gap:10px}
.brand-mark{width:26px;height:26px;border-radius:50%;background:#f7c21c}
.brand-name{font-size:28px;font-weight:400;color:var(--brand-blue)}
.address{position:absolute;right:130px;top:14px;text-align:right;font-style:italic;font-size:16px;line-height:19px;color:var(--brand-blue)}

.main-nav{position:absolute;top:77px;left:0;width:1200px;height:47px;
  background:linear-gradient(180deg,#7e97b2 0%,#9fb4ca 60%,#6f8aa6 100%)}
.nav-list{list-style:none;display:flex;position:absolute;left:128px;top:14px;font-size:17px;color:var(--white)}
.nav-list li{padding:0 8px;border-left:1px solid rgba(255,255,255,.8);line-height:17px}
.nav-list li:first-child{padding-left:0;border-left:none}
.nav-list li:last-child{padding-right:0}

.hero{position:absolute;top:124px;left:0;width:1200px;height:645px;
  background:linear-gradient(180deg,#4d7a3c 0%,#c9813f 18%,#d6b85a 38%,#c9a24e 50%,#7e8a74 62%,#8aa0b6 78%,#7f97b0 100%)}
.hero-fade{position:absolute;left:0;bottom:0;width:1200px;height:170px;
  background:linear-gradient(180deg,rgba(138,160,185,0) 0%,rgba(132,154,180,.8) 40%,#7890ad 100%)}
.feature-cards{position:absolute;top:488px;left:131px;display:flex;gap:21px}
.feature-card{width:298px;height:192px;background:var(--white);padding:6px;position:relative}
.feature-photo{width:100%;height:100%}
.photo-mansion{background:linear-gradient(160deg,#5d7f3e,#c98a55 45%,#3d6a35)}
.photo-pub{background:linear-gradient(120deg,#1e3f7a,#d9b36b 55%,#8b5a2b)}
.photo-pool{background:linear-gradient(180deg,#2c4a7a 0%,#c58b5a 45%,#2bb3c9 75%,#1e8fa8)}
.card-label{position:absolute;left:50%;top:50%;transform:translate(-50%,-50%);width:206px;height:34px;
  border-radius:17px;background:rgba(255,255,255,.6);text-align:center;line-height:34px;font-size:20px;color:#333}
.tagline{position:absolute;top:700px;left:0;width:1200px;text-align:center;font-family:'Raleway',sans-serif;font-weight:300;
  font-size:39px;color:var(--white);letter-spacing:.5px}

.about{top:796px}
.about-title{font-size:19px;font-weight:400;color:var(--heading-grey);margin-bottom:18px}
.about-text{font-size:16px;font-weight:300;line-height:19px;color:var(--text-grey)}
.about-text p{margin-bottom:5px}
.about-text a{color:var(--link-blue);text-decoration:none;font-weight:400}
.location-button{position:absolute;left:0;top:173px;width:136px;height:41px;border-radius:10px;background:var(--accent-orange);
  color:var(--white);font-size:17px;display:flex;align-items:center;padding-left:10px;gap:6px;box-shadow:0 2px 0 #c9461a}
.welcome-note{position:absolute;right:0;top:198px;font-style:italic;font-size:16px;color:var(--accent-gold)}

.footer-nav{position:absolute;top:1040px;left:0;width:1200px;height:39px;
  background:linear-gradient(180deg,#f3f6f9 0%,#c7d4e1 40%,#a2b6ca 100%)}
.footer-nav .nav-list{top:13px;color:var(--footer-link)}
.footer-nav .nav-list li{border-left-color:#9aa9b8}
.footer-nav .nav-list li.current{color:var(--white)}
</style>
</head>
<body>
<header class="site-header">
  <div class="brand"><span class="brand-mark"></span><span class="brand-name">Belcourt Manor</span></div>
  <div class="address">27 Belcourt Drive,<br>Ferndale,Gold Coast,<br>Queensland,Australia</div>
</header>

<nav class="main-nav">
  <ul class="nav-list">
    <li>Main</li><li>Mansion</li><li>Bedrooms</li><li>Options</li><li>Fox and Hare</li><li>Grounds</li><li>Location</li><li>Gallery</li><li>Contact</li><li>Availability</li><li>DIY Weddings</li>
  </ul>
</nav>

<section class="hero" role="img" aria-label="Aerial photo of the yellow manor with terracotta roofs set among palms and lawns">
  <div class="hero-fade"></div>
</section>

<div class="feature-cards">
  <div class="feature-card"><div class="feature-photo photo-mansion" role="img" aria-label="Aerial view of the mansion and pool among gardens"></div><span class="card-label">The Mansion</span></div>
  <div class="feature-card"><div class="feature-photo photo-pub" role="img" aria-label="Private pub interior opening onto a deck at dusk"></div><span class="card-label">The Fox and Hare</span></div>
  <div class="feature-card"><div class="feature-photo photo-pool" role="img" aria-label="Resort pool in front of the house at twilight"></div><span class="card-label">Gallery</span></div>
</div>
<div class="tagline">PALATIAL ESTATE AND LUXURY RESORT</div>

<section class="container about">
  <h2 class="about-title">ABOUT OUR RESORT</h2>
  <div class="about-text">
    <p>On over 2 manicured garden acres, Belcourt Manor is a unique Gold Coast estate, centrally located in the prestigious rural suburb of <a href="#">Ferndale</a>.</p>
    <p>The estate features a grand mansion, private pub <a href="#">(The Fox and Hare)</a>, sparkling resort pool, tennis court and playground.</p>
    <p>Magnificent properties rarely feel so warm and welcoming – so browse away and visit our <a href="#">photo gallery</a>.</p>
    <p>For prices, availability and guest reviews, <a href="#">visit StayNest</a>.</p>
  </div>
  <a class="location-button" href="#">
    <svg width="22" height="26" viewBox="0 0 22 26" aria-hidden="true"><path d="M11 1C5.5 1 1.5 5 1.5 10c0 6.5 9.5 15 9.5 15s9.5-8.5 9.5-15C20.5 5 16.5 1 11 1z" fill="#fff"/><circle cx="11" cy="10" r="3.5" fill="#ee5a24"/></svg>
    Our location
  </a>
  <p class="welcome-note">We look forward to having you stay as our guests.</p>
</section>

<nav class="footer-nav">
  <ul class="nav-list">
    <li class="current">Main</li><li>Mansion</li><li>Bedrooms</li><li>Options</li><li>Fox and Hare</li><li>Grounds</li><li>Location</li><li>Gallery</li><li>Contact</li><li>Availability</li><li>DIY Weddings</li>
  </ul>
</nav>
</body>
</html>
```